2 page Web Site Design (Coded), simple, not picky

I need a web portal for a PPC marketing business. I have the logo, some imagery, and some websites to base the design on.

***Background***
The name of the business is "Quiet Harbor Outreach Advisors" or QHOA. We provide listings in a searchable database for Dental Sleep Medicine doctors. These are doctors who treat snoring/sleep apnea/and CPAP users with oral appliances. Client doctors will have their own "landing page website" where PPC prospects land from the PPC campaigns. Logos for supporting/landing page websites have been uploaded.
***End Background***

THIS website (for you to design) is to introduce doctors to the concept and detail the services. i.e. PPC campaign management services, listing on a national database of Dental Sleep Medicine practitioners, and a fully featured website dedicated to Snoring, Sleep Apnea, and CPAP Alternative treatment (those websites are "Farewell-Rumble.com", "Farewell-NightGasp.com", and ""Farewell-MaskTube.com")

SEM websites whose look I enjoy are:

http://www.brindlequay.com/marketing-services/pay-per-click/

http://www.orchardvantage.com/welcome/pay-per-click-services/

http://www.lanternpeak.com/marketing-services/paid-search-management/

The main colors are Red, White, & Blue. Red and blue used mostly for accents/emphasis.

The main/index page's purpose is to, as best possible, convey the idea of SEM campaign management with supporting websites being their best option for internet marketing!
The secondary page is just a slightly modified layout where details can be explained.

Target Market(s)

Dentists who practice Dental Sleep Medicine (see www.rqtvo.org)

Industry/Entity Type

Marketing

Requirements
Must have
• -Sign-up form for the generation of leads... Simple script that sends E-mail is fine... Doctor's Name, Business Name, Business Address, E-mail address, phone #.

-Graphics that will clearly describe the services being provided.

```html
<!DOCTYPE html>
<html lang="en">
<head>
<meta charset="utf-8">
<title>Quiet Harbor Outreach Advisors – Landing Page</title>
<link rel="stylesheet" href="https://fonts.googleapis.com/css2?family=Arimo:wght@400;700&family=Roboto+Condensed:wght@400;700&display=swap">
<style>
:root{
  --red:#b3262e;
  --red-dark:#8f1a21;
  --blue:#163a7d;
  --blue-dark:#0f2c63;
  --navy-text:#1b3a78;
  --ink:#333;
  --muted:#555;
  --page:#ebebeb;
  --panel:#ffffff;
  --line:#dcdcdc;
}
*{box-sizing:border-box;margin:0;padding:0}
html,body{width:1063px;height:1200px;overflow:hidden}
body{background:var(--page);font-family:"Arimo",Arial,sans-serif;color:var(--ink);position:relative}
a{text-decoration:none}

.site-header{position:absolute;left:0;top:0;width:1063px;height:80px;background:linear-gradient(#fff,#f3f3f3)}
.brand{position:absolute;left:120px;top:0;width:275px;height:138px;background:linear-gradient(#fff,#ececec);border-radius:0 0 8px 8px;box-shadow:0 2px 6px rgba(0,0,0,.35);z-index:3;display:flex;flex-direction:column;align-items:center;justify-content:center;gap:6px;color:var(--red);font-weight:700}
.brand-row{display:flex;align-items:center;gap:10px}
.brand-dot{width:34px;height:34px;border-radius:50%;background:var(--red)}
.brand-short{font-size:38px;letter-spacing:1px}
.brand-full{font-size:11.5px}
.main-nav{position:absolute;top:28px;left:520px;display:flex;font-size:13px}
.main-nav a{color:var(--navy-text);display:block;height:23px;line-height:23px;text-align:center}
.main-nav .current{width:98px;background:linear-gradient(#3a68c0,#163a7d);color:#fff;border-radius:12px;border:1px solid #0e2b60}
.nav-about{margin-left:55px}
.nav-services{margin-left:64px}
.nav-contact{margin-left:56px}

.hero-photo{position:absolute;left:0;top:80px;width:1063px;height:381px;background:radial-gradient(ellipse at 58% 30%,#d9b6a4 0%,#a78274 25%,#6b4a45 50%,#4e4a5a 80%,#7a7e90 100%)}

.sem-card{position:absolute;left:121px;top:184px;width:276px;height:311px;background:var(--red);border:1px solid #d9868a;border-radius:3px;box-shadow:0 3px 8px rgba(0,0,0,.35);color:#fff;z-index:2}
.sem-card header{text-align:center;padding-top:13px;height:66px;border-bottom:1px solid #c9535a}
.sem-card h2{font-family:"Roboto Condensed","Arial Narrow",sans-serif;font-weight:400;font-size:21.5px}
.sem-card .sub{font-size:12px;margin-top:1px}
.sem-card p{font-size:11px;line-height:12.8px;padding:12px 14px 0 13px}
.sem-card ul{list-style:none;font-size:11px;line-height:12.5px;padding:15px 18px 0 40px}
.sem-card li{position:relative;margin-bottom:12px}
.sem-card li::before{content:"";position:absolute;left:-15px;top:3px;border:3px solid transparent;border-left:4px solid #fff}
.btn-more{position:absolute;left:170px;top:275px;width:88px;height:22px;border-radius:11px;background:linear-gradient(#5a8ae0,#163a7d);border:1px solid #0e2b60;color:#fff;font-size:13px;text-align:center;line-height:20px}
.shadow-ellipse{position:absolute;height:10px;border-radius:50%;background:radial-gradient(ellipse,rgba(0,0,0,.25),rgba(0,0,0,0) 70%)}

.promo{position:absolute;left:409px;top:262px;width:532px;height:196px;background:linear-gradient(100deg,#f7f7f7,#dedede);border-radius:3px;border:1px solid #fff;overflow:hidden}
.growth-art{position:absolute;right:0;top:0;width:200px;height:196px;background:linear-gradient(160deg,rgba(255,255,255,0) 0%,rgba(255,255,255,.55) 60%,rgba(255,255,255,.8) 100%)}
.promo h3{position:absolute;left:21px;top:15px;font-weight:400;font-size:22px;color:var(--blue);line-height:25px}
.promo h3 strong{display:block;font-size:20px;font-weight:700}
.promo ul{position:absolute;left:21px;top:75px;width:360px;list-style:none;font-size:10.5px;line-height:12.5px;color:#222}
.promo li{padding-left:13px;position:relative;margin-bottom:8px}
.promo li::before{content:"";position:absolute;left:0;top:3px;width:5px;height:5px;border-left:2px solid var(--red);border-bottom:2px solid var(--red)}
.partners{position:absolute;left:14px;top:155px;display:flex;gap:14px}
.partner{display:flex;align-items:center;gap:4px;font-size:10.5px;font-weight:700;color:var(--blue)}
.partner i{width:14px;height:14px;border-radius:50%;background:var(--blue);display:block}

.content-panel{position:absolute;left:106px;top:484px;width:850px;height:660px;background:var(--panel);border:1px solid var(--line);border-radius:3px}
.col-main{position:absolute;left:128px;top:535px;width:516px;font-size:11px;line-height:16px;color:var(--muted)}
.col-main h1{font-family:"Roboto Condensed","Arial Narrow",sans-serif;font-weight:400;font-size:21.5px;color:#222;padding:0 0 8px 2px;border-bottom:1px solid #ddd;margin-bottom:10px}
.col-main h2{font-size:15.5px;font-weight:700;margin:18px 0 14px}
.h-red{color:var(--red)}
.h-blue{color:var(--navy-text)}
.shots{display:flex;gap:12px;border:1px solid #ccc;padding:4px;width:512px;height:230px;margin-top:15px}
.shot{flex:1;background:linear-gradient(#f4f6fb,#e6eaf2);border:1px solid #d3d3d3}
.col-main ul{list-style:none;margin-top:16px;font-size:10.6px}
.col-main ul li{padding-left:12px;position:relative;color:#333;white-space:nowrap}
.col-main ul li::before{content:"";position:absolute;left:0;top:5px;border:3px solid transparent;border-left:4px solid var(--red)}
.read-more{font-weight:700;color:var(--navy-text);font-size:10px}

.ppc-card{position:absolute;left:659px;top:531px;width:274px;height:259px;background:var(--blue);border-radius:3px;color:#fff}
.ppc-card header{text-align:center;padding-top:12px;height:69px;border-bottom:1px solid #2a4e92}
.ppc-card h2{font-family:"Roboto Condensed","Arial Narrow",sans-serif;font-weight:400;font-size:21.5px}
.ppc-card .sub{font-size:11px;margin-top:2px}
.ppc-card ul{list-style:none;font-size:9.6px;line-height:11.5px;padding:12px 14px 0 39px}
.ppc-card li{position:relative;margin-bottom:13px}
.ppc-card li::before{content:"";position:absolute;left:-13px;top:2px;border:2.5px solid transparent;border-left:3.5px solid #fff}

.signup{position:absolute;left:659px;top:813px;width:274px;height:285px;background:#fff;border:1px solid #ddd;border-radius:3px}
.signup h2{font-family:"Roboto Condensed","Arial Narrow",sans-serif;font-weight:400;font-size:21.5px;color:#222;text-align:center;height:54px;line-height:56px;border-bottom:1px solid #e2e2e2;background:linear-gradient(#fff,#f6f6f6)}
.field{position:absolute;left:18px;font-size:11px;color:#333}
.input{position:absolute;left:125px;width:134px;height:19px;background:linear-gradient(#d2d2d2,#e6e6e6);border:1px solid #c2c2c2;border-radius:3px}
.btn-submit{position:absolute;left:125px;top:249px;width:82px;height:24px;border-radius:12px;background:linear-gradient(#d9434b,#9a1a22);border:1px solid #7a1117;color:#fff;font-size:13px;text-align:center;line-height:22px}

.site-footer{position:absolute;left:108px;top:1159px;font-size:8.5px;line-height:11px;color:#555}
</style>
</head>
<body>

<header class="site-header">
  <nav class="main-nav">
    <a class="current" href="#">Landing Page</a>
    <a class="nav-about" href="#">About</a>
    <a class="nav-services" href="#">Services</a>
    <a class="nav-contact" href="#">Contact</a>
  </nav>
</header>

<div class="brand">
  <div class="brand-row"><span class="brand-dot"></span><span class="brand-short">QHOA LLC</span></div>
  <div class="brand-full">Quiet Harbor Outreach Advisors</div>
</div>

<div class="hero-photo" role="img" aria-label="Photo of a person sleeping peacefully on a pillow"></div>

<section class="sem-card">
  <header>
    <h2>Search Engine Marketing</h2>
    <div class="sub">Online marketing strategy</div>
  </header>
  <p>Search engine marketing is an online marketing strategy that aims to increase qualified visitor traffic to your website by positioning your advertisements at the top and right side of “natural” and “organic” search result pages</p>
  <ul>
    <li>You only pay when someone clicks on one of your advertisements.</li>
    <li>It is estimated that pay per click ads receive around 30% of all clicks on search engines.</li>
    <li>Querybright Ads, Findwell Search Marketing and Lookra Adcenter are pay per click advertising platforms.</li>
  </ul>
  <a class="btn-more" href="#">More</a>
</section>
<div class="shadow-ellipse" style="left:146px;top:500px;width:222px"></div>

<section class="promo">
  <div class="growth-art" role="img" aria-label="Illustration of a rising arrow over a growing bar chart"></div>
  <h3>Customized internet marketing solution<strong>specially designed for OSB Therapists!</strong></h3>
  <ul>
    <li>Will drive customers to your practice with PPC Search engine Marketing and then educate them about the unique benefits inherent to OAT therapy with a dedicated website .</li>
    <li>A fully featured website dedicated to Snoring, Sleep Apnea, and CPAP Alternative treatment</li>
  </ul>
  <div class="partners">
    <span class="partner"><i></i>Farewell-NightGasp.com</span>
    <span class="partner"><i></i>Farewell-Rumble.com</span>
    <span class="partner"><i></i>Farewell-MaskTube.com</span>
  </div>
</section>

<div class="content-panel"></div>

<main class="col-main">
  <h1>Welcome to Quiet Harbor Outreach Advisors</h1>
  <p>will drive customers to your practice with PPC Search engine Marketing and then educate them about the unique benefits inherent to OAT therapy with a dedicated website .</p>
  <h2 class="h-red">What is Search Engine Marketing?</h2>
  <p>Search engine marketing is an online marketing strategy that aims to increase qualified visitor traffic to your website by positioning your advertisements at the top and right side of “natural” and “organic” search result pages [descriptions below].</p>
  <div class="shots">
    <div class="shot" role="img" aria-label="Search results page with the paid pay per click listings highlighted"></div>
    <div class="shot" role="img" aria-label="Search results page with the natural search results highlighted"></div>
  </div>
  <h2 class="h-blue" style="margin-top:22px">Search Engine Marketing(Pay Per Click)</h2>
  <p>Paid search results, called “Pay Per Click” (PPC) advertising, promote websites in “Sponsored” section of search results.</p>
  <ul>
    <li>You only pay when someone clicks on one of your advertisements.</li>
    <li>It is estimated that pay per click ads receive around 30% of all clicks on search engines.</li>
    <li>Querybright Ads, Findwell Search Marketing and Lookra Adcenter are pay per click advertising platforms.</li>
  </ul>
  <a class="read-more" href="#">Read More...</a>
</main>

<aside class="ppc-card">
  <header>
    <h2>Pay Per Click</h2>
    <div class="sub">Search Engine Marketing Campaign Managment.</div>
  </header>
  <ul>
    <li>We set up and manage your search engine marketing campaigns for you.</li>
    <li>You only pay when visitors click on your ad and visit your website.</li>
    <li>We design your ad campaign to optimize ad click conversion rates.</li>
    <li>We send you regular advertising effectiveness monitoring, and analysis reports so you can determine your return-on-investment and adjust your budget accordingly.</li>
  </ul>
</aside>

<form class="signup">
  <h2>Signup Today!</h2>
  <label class="field" style="top:73px">Doctor's Name</label><span class="input" style="top:70px"></span>
  <label class="field" style="top:100px">Business Name</label><span class="input" style="top:97px"></span>
  <label class="field" style="top:128px">Business Address</label><span class="input" style="top:124px;height:57px"></span>
  <label class="field" style="top:194px;left:21px">E-mail address</label><span class="input" style="top:190px"></span>
  <label class="field" style="top:221px;left:18px">Phone.No</label><span class="input" style="top:217px"></span>
  <span class="btn-submit">Submit</span>
</form>
<div class="shadow-ellipse" style="left:683px;top:1095px;width:224px"></div>

<footer class="site-footer">Copyrights@Quiet Harbor Outreach Advisors.com<br>All rights reserved.</footer>

</body>
</html>
```